Property letting UK website

I need a web design for a new Property letting company in the UK. I already have a logo that was produced and won by a brief forge logo designer last week.

I like modern designs and require ease of functionality and usage. I already have a domain name registered so need to be able to link to that domain.

Regards,

Morven.

Target Market(s)

UK property

Industry/Entity Type

It Company

Number of Pages Required

5+ page

Requirements
Must have
• Home page, Current properties to let page, About us page, Contact us page, Testimonials page and ability to link to twitter and Facebook account.

```html
<!DOCTYPE html>
<html lang="en">
<head>
<meta charset="utf-8">
<title>Nestwell – Residential Property Management</title>
<link href="https://fonts.googleapis.com/css2?family=Lato:wght@300;400;700&family=Noto+Serif:ital,wght@0,400;1,400&family=Arimo:wght@400&display=swap" rel="stylesheet">
<style>
:root{
  --black:#050505;
  --sky:#0aa5e6;
  --navy:#0a3f78;
  --navy-deep:#062d5a;
  --navy-light:#1162a6;
  --page:#f4f4f4;
  --text:#333;
  --muted:#555;
  --footer:#2b2b2b;
  --footer-deep:#1c1c1c;
  --white:#fff;
}
*{margin:0;padding:0;box-sizing:border-box}
html,body{width:849px;height:1200px;overflow:hidden}
body{position:relative;background:var(--page);font-family:"Lato",sans-serif;color:var(--text)}
.abs{position:absolute}

/* header */
.site-header{left:0;top:0;width:849px;height:75px;background:var(--black)}
.brand{left:110px;top:18px;display:flex;align-items:center;gap:8px;color:var(--white);font-family:"Lato",sans-serif;font-weight:300;font-size:30px;letter-spacing:1px}
.brand-dot{width:12px;height:12px;border-radius:50%;background:var(--sky)}
.main-nav{left:312px;top:31px;display:flex;align-items:center;font-size:9px;color:var(--white)}
.main-nav span{margin-right:16px}
.main-nav .active{background:var(--sky);border-radius:4px;width:59px;height:22px;line-height:22px;text-align:center;margin-right:16px}

/* hero */
.hero{left:0;top:75px;width:849px;height:146px;background:linear-gradient(90deg,#9a8a78 0%,#b86a4a 35%,#7c6a5a 55%,#5e8a3a 80%,#8cb04a 100%)}
.hero-caption{left:378px;top:123px;width:378px;height:60px;background:rgba(20,20,20,.72);color:var(--white);font-family:"Noto Serif",serif;padding:8px 0 0 16px;line-height:24px}
.hero-caption .l1{font-size:16px;text-transform:uppercase}
.hero-caption .l2{font-size:19px}

/* services */
.services{left:0;top:221px;width:849px;height:208px;background:linear-gradient(180deg,var(--navy-deep),var(--navy) 50%,var(--navy-light))}
.service{width:220px;text-align:center;color:var(--white)}
.service .icon{width:80px;height:80px;border-radius:50%;background:var(--white);margin:0 auto;display:flex;align-items:center;justify-content:center}
.service h3{font-family:"Noto Serif",serif;font-weight:400;font-size:14px;margin-top:14px}
.service p{font-size:11px;line-height:16px;margin-top:6px;color:#e6eef6}
.read-more{display:inline-block;margin-top:10px;background:linear-gradient(#fff,#ccc);color:var(--navy-deep);font-family:"Noto Serif",serif;font-style:italic;font-size:11px;padding:1px 7px;border:1px solid #999}
.divider{top:245px;width:1px;height:150px;background:rgba(255,255,255,.12)}

/* about */
.about-title{left:115px;top:446px;font-size:17px;color:var(--sky);font-weight:300}
.about-title b{font-size:24px;font-weight:300}
.about-text{left:115px;width:416px;font-family:"Arimo",sans-serif;font-size:8.3px;line-height:14.5px;color:var(--muted);text-align:justify}

/* quick search */
.search-box{left:577px;top:437px;width:175px;height:234px;background:var(--white);border-radius:6px;padding:10px 14px}
.search-box h4{font-weight:400;font-size:13px;color:var(--sky)}
.field{position:absolute;height:14px;border:1px solid #bbb;font-family:"Arimo",sans-serif;font-size:7.5px;line-height:12px;padding-left:3px;background:var(--white)}
.field::after{content:"▾";position:absolute;right:3px;top:0;color:#222}
.radio{position:absolute;top:62px;font-size:8px;color:var(--sky);display:flex;align-items:center;gap:5px}
.radio i{width:12px;height:12px;border-radius:50%;border:1px solid #999;background:#eee;display:inline-block}
.radio i.on{background:radial-gradient(#555 30%,#eee 35%)}
.suburbs{position:absolute;left:18px;top:163px;width:139px;height:52px;border:1px solid #bbb;font-family:"Arimo",sans-serif;font-size:7.5px;line-height:10.5px;overflow:hidden}
.suburbs div{padding-left:2px}
.suburbs .sel{background:#ddd}
.search-btn{left:675px;top:659px;width:59px;height:23px;border-radius:4px;background:var(--sky);color:var(--white);font-size:9px;line-height:23px;text-align:center}

/* projects */
.projects-line{left:160px;top:706px;width:550px;height:1px;background:#c9d6e3}
.projects-tab{left:335px;top:706px;width:200px;height:22px}
.projects-tab span{position:absolute;left:0;top:0;width:200px;text-align:center;color:var(--white);font-weight:700;font-size:13px;line-height:22px}
.carousel{left:105px;top:749px;width:651px;height:124px;background:linear-gradient(#e9e9e9,#f7f7f7);box-shadow:0 3px 3px rgba(0,0,0,.25)}
.card{top:761px;width:134px;height:98px;border:1px solid #9bb3cc}
.card .cap{position:absolute;left:0;bottom:0;width:100%;height:25px;background:rgba(10,100,180,.85);color:var(--white);font-size:8px;line-height:10px;padding:3px 7px}
.card .cap em{font-weight:700}
.arrow{top:802px;width:18px;height:18px;border-radius:50%;background:var(--navy);display:flex;align-items:center;justify-content:center}

/* footer */
.footer{left:0;top:985px;width:849px;height:215px;background:linear-gradient(var(--footer),var(--footer-deep))}
.footer-brand{left:423px;top:1000px;color:var(--white);font-weight:300;font-size:24px;display:flex;align-items:center;gap:6px}
.footer h5{position:absolute;top:1044px;color:var(--white);font-weight:400;font-size:12.5px;padding-bottom:5px;border-bottom:1px solid #444}
.links{left:94px;top:1068px;font-size:9px;line-height:19.5px;color:#ddd}
.links div::before{content:"› ";color:#aaa}
.newsletter{left:233px;top:1068px;width:155px;font-size:9px;line-height:13px;color:#ddd}
.email-input{left:233px;top:1102px;width:153px;height:19px;background:var(--white);font-size:8.5px;color:#888;padding:4px 6px}
.subscribe{left:233px;top:1128px;width:74px;height:20px;background:linear-gradient(#f4f4f4,#bbb);color:#333;font-size:10.5px;font-weight:700;text-align:center;line-height:20px;letter-spacing:.5px}
.contact{left:423px;font-size:9px;color:#ddd;display:flex;align-items:flex-start;gap:8px}
.contact.big{font-size:10.5px;font-weight:700;color:var(--white)}
.map{left:579px;top:1069px;width:177px;height:88px;background:linear-gradient(135deg,#f2ebd9,#e3dcc8 40%,#bcd3e6 70%,#d9e5c7);border:2px solid #fff}
.footer-rule{left:0;top:1172px;width:849px;height:1px;background:#3c3c3c}
.follow{left:94px;top:1178px;color:var(--white);font-size:12px;display:flex;align-items:center;gap:5px}
.follow i{width:19px;height:19px;border-radius:50%;display:inline-block;background:#555}
.copyright{left:420px;top:1184px;font-size:8.5px;color:#ddd}
</style>
</head>
<body>

<header class="abs site-header"></header>
<div class="abs brand"><span class="brand-dot"></span>Nestwell</div>
<nav class="abs main-nav">
  <span class="active">Home</span><span>Buy</span><span>Sell</span><span>Rent</span><span>Testimonials</span><span>About Us</span><span>Services</span><span>Contact Us</span>
</nav>

<div class="abs hero" role="img" aria-label="Photograph of modern brick apartment building with steps, glass balcony and green lawn"></div>
<div class="abs hero-caption"><div class="l1">We are a residential property</div><div class="l2">Management &amp; Consulting Company.</div></div>

<section class="abs services"></section>
<div class="abs divider" style="left:307px"></div>
<div class="abs divider" style="left:545px"></div>

<div class="abs service" style="left:78px;top:236px">
  <div class="icon"><svg width="34" height="34" viewBox="0 0 34 34"><path d="M6 28 L24 10 M10 6 L28 26" stroke="#111" stroke-width="4" stroke-linecap="round"/><circle cx="25" cy="8" r="5" fill="none" stroke="#111" stroke-width="3"/></svg></div>
  <h3>PROPERTY MANAGEMENT</h3>
  <p>Lorem ipsum dolor sit amet,<br>consectetuer adipiscing consequat.</p>
  <span class="read-more">Read More</span>
</div>
<div class="abs service" style="left:316px;top:236px">
  <div class="icon"><svg width="36" height="30" viewBox="0 0 36 30"><path d="M2 12 L12 4 L20 10 L26 4 L34 12 L20 26 Z" fill="#111"/></svg></div>
  <h3>PROPERTY CONSULTING</h3>
  <p>Lorem ipsum dolor sit amet,<br>consectetuer adipiscing consequat.</p>
  <span class="read-more">Read More</span>
</div>
<div class="abs service" style="left:552px;top:236px">
  <div class="icon"><svg width="34" height="32" viewBox="0 0 34 32"><path d="M9 14 L17 6 L25 14 V22 H9 Z" fill="none" stroke="#111" stroke-width="2.5"/><path d="M3 24 Q12 20 17 26 L31 22 L30 28 L16 31 L3 28 Z" fill="#111"/></svg></div>
  <h3>OTHER SERVICES</h3>
  <p>Lorem ipsum dolor sit amet,<br>consectetuer adipiscing consequat.</p>
  <span class="read-more">Read More</span>
</div>

<h2 class="abs about-title">About <b>Nestwell</b></h2>
<p class="abs about-text" style="top:475px">Lorem ipsum dolor sit amet, consectetur adipiscing elit. Sed vitae nisi metus. Quisque quis nibh at risus mollis commodo. Vivamus hendrerit sit amet nulla ac commodo. Curabitur a laoreet augue. Aenean sed vestibulum arcu, eu posuere ex. Nam scelerisque porta risus, eu iaculis urna porta quis. In cursus diam vitae eros feugiat ultricies. Maecenas id nulla magna. Vivamus varius ligula tellus, id placerat eros egestas ut. Sed imperdiet elit vel mollis cursus. Curabitur aliquam posuere purus in fermentum. Nulla suscipit nunc tempor lacinia molestie. Ut eget leo sed lorem iaculis ullamcorper. Suspendisse fringilla, nibh vitae volutpat facilisis, metus nisi finibus libero, nec rutrum est risus sed massa.</p>
<p class="abs about-text" style="top:594px">Nulla lacinia lacus aliquam nibh ullamcorper gravida. Vivamus a nunc venenatis, imperdiet magna vitae, eleifend nisi. Nulla odio elit, sodales laoreet risus ut, efficitur euismod neque. Vestibulum egestas aliquam velit, vel hendrerit magna fermentum vitae. Sed molestie orci et urna imperdiet accumsan. Vivamus eget ex in diam tristique malesuada quis id est. Donec nec mauris eget enim malesuada fermentum. Sed ultricies urna eget nisl suscipit, eget ornare diam euismod. Nulla accumsan orci eu risus tristique imperdiet. Duis interdum, mi non convallis fringilla, arcu turpis interdum nisi, et sagittis risus mi id tortor. Pellentesque bibendum pharetra arcu sed vestibulum.</p>

<aside class="abs search-box">
  <h4>Quick Search</h4>
  <div class="field" style="left:18px;top:35px;width:139px">Residential Search</div>
  <div class="radio" style="left:22px"><i class="on"></i>BUY</div>
  <div class="radio" style="left:64px"><i></i>RENT</div>
  <div class="field" style="left:18px;top:90px;width:65px">Price Min</div>
  <div class="field" style="left:91px;top:90px;width:64px">Price Max</div>
  <div class="field" style="left:18px;top:117px;width:65px">Bedrooms</div>
  <div class="field" style="left:91px;top:118px;width:64px">Bathrooms</div>
  <div class="field" style="left:18px;top:143px;width:139px">All Types</div>
  <div class="suburbs"><div class="sel">All Suburbs</div><div>Abbey</div><div>Alfred Cove</div><div>Armadale</div><div>Attadale</div></div>
</aside>
<div class="abs search-btn">Search</div>

<div class="abs projects-line"></div>
<svg class="abs projects-tab" viewBox="0 0 200 22" width="200" height="22"><path d="M0 0 H200 L185 22 H15 Z" fill="#0b5ea8"/><span></span></svg>
<div class="abs projects-tab"><span>Our Projects</span></div>

<div class="abs carousel"></div>
<div class="abs card" style="left:142px;background:linear-gradient(#8fb6e0,#dfe6ee 55%,#6a7d94)" role="img" aria-label="Photograph of a modern office building">
  <div class="cap"><em>Project Name</em><br>Duis autem vel eum</div></div>
<div class="abs card" style="left:290px;background:linear-gradient(#a14a35,#c08a6a 55%,#7a6a5a)" role="img" aria-label="Photograph of brick townhouses">
  <div class="cap"><em>Project Name</em><br>Duis autem vel eum</div></div>
<div class="abs card" style="left:436px;background:linear-gradient(#b6cde0,#c9a97a 55%,#6f7a5a)" role="img" aria-label="Photograph of a villa with palm trees">
  <div class="cap"><em>Project Name</em><br>Duis autem vel eum</div></div>
<div class="abs card" style="left:584px;background:linear-gradient(#c8d3de,#9aa4ae 55%,#b2582e)" role="img" aria-label="Photograph of city high-rise towers">
  <div class="cap"><em>Project Name</em><br>Duis autem vel eum</div></div>
<div class="abs arrow" style="left:115px"><svg width="8" height="8" viewBox="0 0 8 8"><path d="M6 1 L2 4 L6 7" stroke="#fff" stroke-width="1.6" fill="none"/></svg></div>
<div class="abs arrow" style="left:727px"><svg width="8" height="8" viewBox="0 0 8 8"><path d="M2 1 L6 4 L2 7" stroke="#fff" stroke-width="1.6" fill="none"/></svg></div>

<footer class="abs footer"></footer>
<svg class="abs" style="left:0;top:975px" width="849" height="60" viewBox="0 0 849 60">
  <path d="M0 10 H849 V0 H0 Z" fill="var(--page)"/>
  <path d="M85 10 Q220 50 400 10 Z" fill="var(--page)"/>
  <path d="M120 10 Q260 40 405 10" stroke="#0b5ea8" stroke-width="5" fill="none"/>
  <path d="M740 10 Q800 20 849 50 V36 Q800 12 770 10 Z" fill="#8a8a8a"/>
</svg>
<div class="abs footer-brand"><span class="brand-dot"></span>Nestwell</div>

<h5 style="left:94px">QUICK LINKS</h5>
<h5 style="left:233px">NEWSLETTER SIGNUP</h5>
<h5 style="left:423px">CONTACT DETAIL</h5>

<div class="abs links"><div>Home</div><div>About Us</div><div>Property Management</div><div>Property Consulting</div><div>Contact</div></div>
<div class="abs newsletter">Stay connected and receive email updates from Nestwell</div>
<div class="abs email-input">Enter your email here</div>
<div class="abs subscribe">SUBSCRIBE</div>

<div class="abs contact" style="top:1068px"><svg width="10" height="13" viewBox="0 0 10 13"><path d="M5 13 L1 6 A4 4 0 1 1 9 6 Z" fill="#fff"/><circle cx="5" cy="5" r="1.6" fill="#222"/></svg><span>123 PG Duis aute irur dolore<br>srephenderit amit in voluptate</span></div>
<div class="abs contact big" style="top:1102px"><svg width="10" height="10" viewBox="0 0 10 10"><path d="M2 0 L4 3 L3 4 Q4 6 6 7 L7 6 L10 8 L8 10 Q2 9 0 2 Z" fill="#fff"/></svg>020 7946 0321</div>
<div class="abs contact big" style="top:1125px"><svg width="11" height="10" viewBox="0 0 11 10"><rect x="2" y="0" width="7" height="3" fill="#fff"/><rect x="0" y="3" width="11" height="5" fill="#fff"/><rect x="2" y="6" width="7" height="4" fill="#fff" stroke="#222"/></svg>020 7946 0321</div>
<div class="abs contact" style="top:1147px"><svg width="10" height="8" viewBox="0 0 10 8"><rect width="10" height="8" fill="#fff"/><path d="M0 0 L5 4 L10 0" stroke="#222" fill="none"/></svg>hello@nestwell-lets.co.uk</div>

<div class="abs map" role="img" aria-label="Street map showing the office location with a pin marker"></div>

<div class="abs footer-rule"></div>
<div class="abs follow">Follow Us :&nbsp;<i></i><i></i><i></i><i></i></div>
<div class="abs copyright">Copyright © 2014 - www.nestwell-lets.co.uk - All rights reserved.</div>

</body>
</html>
```